QV - menu design

Hi,

We require elegant menu design for upscale restaurant. Please find attached the logo and the menu items for your reference.

for inspiration, this is a good website: -
http://www.platewhisper.example/bellfoldnotes/about.php

We are very much open for Menu Size suggestions.

unfortunately the place is going under renovation, we don't have updated images to it. the closest look and feel to our place is http://varnelo.example ..

we are also open for creative options on the shape, the styles, etc. as long as it represents the fine dine feel ...

Thanks ...

Dear All,

We wouldlike to extend our apology for not being able to provide feedbacks on everysingle design. We were extremely busy and we have multiple contests opensimultaneously which makes the process even harder.

However,we would like to thank you all for the efforts you have put into designingour menu. It is very much appreciated …

We wishyou all success in your design ventures and we are quite positive that we willbe working with many of you on many projects in the soon future. 

Thanks & Regards,

TLG Team...

 

 

 

Industry/Entity Type

Restaurant

Requirements
Must have
• Please ensure that there are 'some' images in the menu ... this is very important.
Should not have
• IMPORTANT: -

1. Please DO NOT insert any currency sign to the menu
2. Please keep the prices of the menu at the end of the menu items descriptions NOT beside the menu item names. The font of the price should be similar to the menu item description and please DO NOT bold the numbers. the prices should be subtle.

Thank you ...

```html
<!DOCTYPE html>
<html lang="en">
<head>
<meta charset="utf-8">
<title>QV Cafe – Menu</title>
<link rel="stylesheet" href="https://fonts.googleapis.com/css2?family=Cinzel:wght@700&family=Almendra:ital,wght@1,700&family=Open+Sans:wght@400;600&display=swap">
<style>
  :root{
    --stage:#3a3129;
    --stage-low:#5a4a38;
    --panel:#7d6649;
    --panel-light:#8d7656;
    --panel-edge:#5e4a33;
    --ink:#3a2816;
    --item:#54401f;
    --heading:#6a1c12;
    --swirl:rgba(214,190,150,.22);
    --cover:#2b2828;
    --cover-ink:#ffffff;
    --cover-gold:#b49a72;
  }
  *{box-sizing:border-box;margin:0;padding:0}
  html,body{width:1200px;height:900px;overflow:hidden}
  body{
    background:linear-gradient(180deg,var(--stage) 0%,var(--stage-low) 100%);
    position:relative;
    font-family:"Open Sans",sans-serif;
    color:var(--ink);
  }
  .panel{
    position:absolute;top:70px;width:350px;height:760px;
    background:linear-gradient(160deg,var(--panel-light),var(--panel));
    overflow:hidden;
  }
  .panel--breakfast{left:70px;border-right:1px solid var(--panel-edge)}
  .panel--drinks{left:420px}
  .panel--cover{left:830px;width:300px;background:var(--cover)}
  .swirl-pattern{
    position:absolute;inset:0;
    background:
      radial-gradient(ellipse 60% 25% at 30% 40%,var(--swirl),transparent 70%),
      radial-gradient(ellipse 50% 30% at 70% 75%,var(--swirl),transparent 70%),
      radial-gradient(ellipse 40% 20% at 60% 20%,var(--swirl),transparent 70%);
  }
  .content{position:relative;padding:28px 28px 0}
  .section-title{
    position:relative;text-align:center;
    font-family:"Cinzel",serif;font-weight:700;font-size:15px;
    color:var(--heading);letter-spacing:.5px;
    padding:14px 0 10px;margin-bottom:12px;
  }
  .title-flourish{
    position:absolute;left:50%;top:4px;transform:translateX(-50%);
    width:190px;height:36px;border-radius:18px;
    background:linear-gradient(90deg,transparent,rgba(70,45,25,.35),transparent);
  }
  .section-title span{position:relative}
  .dish{margin-bottom:17px}
  .dish-name{
    font-family:"Almendra",serif;font-style:italic;font-weight:700;
    font-size:15px;color:var(--item);margin-bottom:3px;
  }
  .dish-desc{font-size:11.5px;line-height:1.42}
  .drinks .section-title{margin-top:6px;margin-bottom:6px}
  .price-cols{display:flex;justify-content:space-between;font-size:11px;line-height:1.45;margin-bottom:8px}
  .price-cols ul{list-style:none}
  .price-cols ul:last-child{text-align:right}
  .cover-flourish{
    position:absolute;left:40px;width:220px;height:46px;border-radius:23px;
    background:linear-gradient(90deg,transparent,var(--cover-gold),transparent);opacity:.55;
  }
  .cover-flourish--top{top:240px}
  .cover-flourish--bottom{top:420px}
  .brand{
    position:absolute;left:0;right:0;top:318px;text-align:center;
    color:var(--cover-ink);font-family:"Open Sans",sans-serif;font-weight:400;
  }
  .brand-name{font-size:38px;letter-spacing:10px;line-height:1}
  .brand-sub{font-size:11px;letter-spacing:6px;margin-top:8px}
</style>
</head>
<body>

<section class="panel panel--breakfast">
  <div class="swirl-pattern" role="img" aria-label="Faint light swirl ornament pattern"></div>
  <div class="content">
    <h2 class="section-title"><i class="title-flourish" role="img" aria-label="Scroll ornament frame"></i><span>THE BREAKFAST</span></h2>
    <article class="dish"><h3 class="dish-name">Butter Croissant</h3>
      <p class="dish-desc">Served plain with a selection of two jams, a vanilla custard cream, a chocolate cream and butter curls. 36</p></article>
    <article class="dish"><h3 class="dish-name">Cheese Croissant</h3>
      <p class="dish-desc">Crumbly freshly baked with cheese filling. 29</p></article>
    <article class="dish"><h3 class="dish-name">Daily Fresh Eggs</h3>
      <p class="dish-desc">A choice of poached, scrambled, pan fried, omelet; all served with toasted bread, mushrooms, roasted tomatoes and chicken sausages. 59</p></article>
    <article class="dish"><h3 class="dish-name">Healthy Time</h3>
      <p class="dish-desc">One choice of hot beverage from our cafe served with fruit salad, natural yoghurt, whole wheat bread vegetable sandwiches and sugar free biscuits selection. 49</p></article>
    <article class="dish"><h3 class="dish-name">Energy Time</h3>
      <p class="dish-desc">One choice of hot beverage from our cafe served with finger chocolate muffins, poached egg with toasted bread and crispy beef bacon, crepe roll with goat cheese and honey and finger chocolate cream with salted cookies. 59</p></article>
    <article class="dish"><h3 class="dish-name">QV Time</h3>
      <p class="dish-desc">One choice of hot beverage from our cafe served with our selection of scones, smoked salmon and avocado sandwich, roasted sausages sandwich, grilled vegetables sandwich, selection of our best biscuits. 59</p></article>
    <article class="dish"><h3 class="dish-name">The Arabic Breakfast</h3>
      <p class="dish-desc">Choice of zattar manakish and cheese manakish served with one choice of hot beverage from our cafe and fresh orange juice. 59</p></article>
  </div>
</section>

<section class="panel panel--drinks drinks">
  <div class="swirl-pattern" role="img" aria-label="Faint light swirl ornament pattern"></div>
  <div class="content">
    <h2 class="section-title"><i class="title-flourish" role="img" aria-label="Scroll ornament frame"></i><span>COFFEE</span></h2>
    <div class="price-cols">
      <ul><li>Coffee Americano 30</li><li>Latte Macchiato 35</li><li>Espresso Doppio 25</li><li>Espresso Macchiato 25</li><li>Cappuccino Viennese 30</li></ul>
      <ul><li>Cappuccino 30</li><li>Espresso 20</li><li>Mocha Frappe 35</li><li>Hot Chocolate 30</li><li>Turkish coffee 25</li></ul>
    </div>
    <h2 class="section-title"><i class="title-flourish" role="img" aria-label="Scroll ornament frame"></i><span>ICED TEA</span></h2>
    <div class="price-cols">
      <ul><li>Peach 35</li></ul>
      <ul><li>Lemon 35</li></ul>
    </div>
    <h2 class="section-title"><i class="title-flourish" role="img" aria-label="Scroll ornament frame"></i><span>TEA</span></h2>
    <div class="price-cols">
      <ul><li>English Breakfast 35</li><li>Earl Grey 35</li><li>Mint 35</li><li>Herbal 35</li></ul>
      <ul><li>Pure Green tea 35</li><li>Jasmine 35</li><li>Peppermint 35</li></ul>
    </div>
    <h2 class="section-title"><i class="title-flourish" role="img" aria-label="Scroll ornament frame"></i><span>WATER / SODA</span></h2>
    <div class="price-cols">
      <ul><li>Cola Nova 20</li><li>Zestra 20</li><li>Ginger Ale 20</li><li>Vigor Buck 45</li><li>Belvaux 75cl 30</li><li>Alpelle 75cl 30</li></ul>
      <ul><li>Diet Cola Nova 20</li><li>Diet Zestra 20</li><li>Orangeo 20</li><li>Belvaux 33cl 20</li><li>Alpelle 33cl 20</li></ul>
    </div>
  </div>
</section>

<section class="panel panel--cover">
  <div class="cover-flourish cover-flourish--top" role="img" aria-label="Gold scroll ornament"></div>
  <div class="brand">
    <div class="brand-name">QV</div>
    <div class="brand-sub">CAFE</div>
  </div>
  <div class="cover-flourish cover-flourish--bottom" role="img" aria-label="Gold scroll ornament"></div>
</section>

</body>
</html>
```